Quarterly real estate newsletter

I need to update the layout of my newsletter so that the address can be printed on the newsletter itself. I also need to update the overall design. I need a template that I can use to edit the content going forward. This will be mailed to owners of homes worth $2,000,000 or more, so needs to be very polished and professional looking.
Below is the printer template that I need to use. Also is the last newsletter I sent, in Publisher format. The Juniper Digest is a partial conversion to the new template, but still needs a lot of work. That is not how I want the final version to look.
On the cover, instead of a graph at the bottom, I would like a graphic with a few key market statistics (e.g. Median price, homes sold, average days on market) with some nice graphical elements, large arrows point up or down.
Inside I would like:
- an article with photos
- A list of recent solds
- our photo quiz
- a chart (like the one currently on the front)
- a second article (if there is room)
- contact info
The back is okay, although I think it could look a little cleaner
Target Market(s)
San Francisco home owners
Industry/Entity Type
Real Estate
Colors
Look and feel

```html
<!DOCTYPE html>
<html lang="en">
<head>
<meta charset="utf-8">
<title>Juniper Digest Update – Issue No. 05</title>
<link href="https://fonts.googleapis.com/css2?family=Archivo+Black&family=Archivo:wght@400;500;600;700&display=swap" rel="stylesheet">
<style>
  :root{
    --navy:#3b4468;
    --navy-band:rgba(58,70,112,.88);
    --ink:#2b2b2f;
    --paper:#ffffff;
    --backdrop:#e9eae7;
    --snapshot:#dedbdd;
    --green:#2e8b3e;
    --lime:#8cbf2a;
    --red:#d9434a;
    --muted:#6c6c74;
  }
  *{box-sizing:border-box;margin:0;padding:0}
  html,body{width:1200px;height:1200px;overflow:hidden;background:var(--backdrop)}
  body{font-family:"Archivo",Arial,sans-serif;color:var(--ink)}
  .page{position:absolute;left:225px;top:18px;width:750px;height:1164px;background:var(--paper);box-shadow:0 2px 10px rgba(0,0,0,.12)}
  .tagline{position:absolute;top:30px;left:0;width:100%;text-align:center;font-size:21px;color:#3a3a40}
  .masthead{position:absolute;top:72px;left:27px;width:685px;font-family:"Archivo Black",Arial,sans-serif;font-size:44px;letter-spacing:1.5px;color:var(--navy);white-space:nowrap;text-align:center}
  .issue{position:absolute;top:132px;right:38px;font-size:14px;color:var(--navy);letter-spacing:.3px}
  .hero{position:absolute;left:27px;top:165px;width:685px;height:425px;background:linear-gradient(180deg,#1b3f9c 0%,#3a70c8 28%,#b98a5e 46%,#6d6258 56%,#9aa3ad 70%,#cfd6de 84%,#5d6a78 100%)}
  .hero-band{position:absolute;left:27px;top:524px;width:560px;height:66px;background:var(--navy-band);clip-path:polygon(0 0,88% 0,100% 100%,0 100%)}
  .hero-title{position:absolute;left:40px;top:536px;font-family:"Archivo",Arial,sans-serif;font-weight:600;font-size:36px;color:#fff;letter-spacing:.5px}
  .article{position:absolute;left:27px;top:612px;width:473px;font-size:11.6px;line-height:1.58;text-align:justify;hyphens:auto}
  .article p+p{margin-top:14px}
  .agent-photo{position:absolute;left:555px;top:606px;width:157px;height:200px;background:linear-gradient(180deg,#6f8a3a 0%,#b59a7a 45%,#8eb2cf 100%)}
  .agent{position:absolute;left:548px;top:814px;width:172px}
  .agent-name{font-weight:700;font-size:21px;color:#222;letter-spacing:-.3px;white-space:nowrap}
  .agent-role{font-size:12px;margin-top:3px;white-space:nowrap}
  .agent-line{font-size:12px;margin-top:5px;white-space:nowrap}
  .brokerage{margin-top:14px;display:flex;align-items:center;gap:7px;font-weight:600;font-size:16px;color:var(--navy);white-space:nowrap}
  .brokerage .mark{width:11px;height:11px;background:var(--navy);flex:none}
  .snapshot{position:absolute;left:27px;top:990px;width:685px;height:132px;background:var(--snapshot);display:flex;align-items:center}
  .snapshot-title{width:186px;padding-left:18px;color:var(--navy);border-right:1.5px solid #b9b6bb;height:96px;display:flex;flex-direction:column;justify-content:center;line-height:1}
  .snapshot-title .q{font-weight:600;font-size:22px}
  .snapshot-title .big{font-weight:600;font-size:34px;letter-spacing:.5px}
  .snapshot-title .sub{font-weight:600;font-size:26px;letter-spacing:.5px;margin-top:4px}
  .stat{flex:1;text-align:center;display:flex;flex-direction:column;align-items:center}
  .stat svg{height:46px;width:50px;margin-bottom:6px}
  .stat-value{font-family:"Archivo Black",Arial,sans-serif;font-size:22px;color:#222;letter-spacing:.8px}
  .stat-label{font-size:9.5px;margin-top:4px;color:#333}
</style>
</head>
<body>
<main class="page">
  <p class="tagline">The Latest Real Estate News and Listings</p>
  <h1 class="masthead">JUNIPER DIGEST UPDATE</h1>
  <p class="issue">ISSUE NO. 05 -&nbsp; SEPT. 2016</p>

  <div class="hero" role="img" aria-label="Harbor full of moored sailboats beneath snow-dusted mountains at sunset"></div>
  <div class="hero-band"></div>
  <h2 class="hero-title">Second Quarter in Review</h2>

  <section class="article">
    <p>Since 2012, San Francisco’s overall average sales price has shown tremendous growth year over year. With San Francisco leading the charge after the 2008 market recession, available inventory dwindled and sales prices climbed annually throughout the City. However, second quarter 2016 data from the San Francisco Multiple Listing Service reflected that, while the San Francisco real estate market remains vibrant and strong, there has been a shift in direction.</p>
    <p>After seeing significant year-over-year gains, the average sales price throughout San Francisco for single-family homes fell slightly, 2.8 percent, decreasing from an average of $1.79 million in the second quarter of 2015, to an average of $1.74 million in the second quarter of 2016. In our review of seven major districts in the City, we found the average sales price in the second quarter of 2016 for a single-family home decreased in five of them, compared to the second quarter of 2015. In four of the seven districts we analyzed, the average sales price year-over-year for a condominium saw a decline. Throughout the City, condominiums saw a 2.2 percent drop in average sales price, with the average sales price at $1.36 million in the second quarter of 2015, to the average of $1.29 million in the second quarter of 2016.</p>
  </section>

  <div class="agent-photo" role="img" aria-label="Portrait of the agent outdoors"></div>
  <aside class="agent">
    <p class="agent-name">Daniel Corwin</p>
    <p class="agent-role">Luxury Property Specialist</p>
    <p class="agent-line">415.555.0142</p>
    <p class="agent-line">daniel@jd-sf.com</p>
    <p class="agent-line">www.jd-sf.com</p>
    <p class="brokerage"><span class="mark"></span>Harborline Realty</p>
  </aside>

  <section class="snapshot">
    <div class="snapshot-title"><span class="q">Q2</span><span class="big">MARKET</span><span class="sub">SNAPSHOT</span></div>
    <div class="stat">
      <svg viewBox="0 0 50 46" aria-hidden="true"><path d="M25 4 2 24h7v19h12V31h8v12h12V24h7z" fill="var(--green)"/></svg>
      <span class="stat-value">1112</span><span class="stat-label">Listed Properties</span>
    </div>
    <div class="stat">
      <svg viewBox="0 0 50 46" aria-hidden="true"><circle cx="25" cy="23" r="21" fill="var(--lime)"/><text x="25" y="32" text-anchor="middle" font-family="Archivo,Arial,sans-serif" font-weight="700" font-size="26" fill="#fff">$</text></svg>
      <span class="stat-value">$200K</span><span class="stat-label">Average Sale Price</span>
    </div>
    <div class="stat">
      <svg viewBox="0 0 50 46" aria-hidden="true" fill="none" stroke="var(--navy)" stroke-width="2.6"><rect x="3" y="7" width="32" height="28" rx="2"/><path d="M3 15h32M11 3v8M27 3v8"/><path d="M9 21h4M17 21h4M25 21h4M9 28h4M17 28h4" stroke-width="3"/><circle cx="36" cy="33" r="10" fill="#fff"/><path d="M36 27v6h5"/></svg>
      <span class="stat-value">41</span><span class="stat-label">Days on Market</span>
    </div>
    <div class="stat">
      <svg viewBox="0 0 50 46" aria-hidden="true"><path d="M25 3 4 20v23h42V20z" fill="none" stroke="var(--red)" stroke-width="3"/><rect x="11" y="22" width="28" height="12" fill="var(--red)"/></svg>
      <span class="stat-value">781</span><span class="stat-label">Sold Properties</span>
    </div>
  </section>
</main>
</body>
</html>
```